Letterhead and Stationary for Construction Company

Brisk Current needs modern Letterhead, Envelopes and Notepad designs.

Industry/Entity Type

Construction

Colors
f78f20
34a7d8
ffffff

Requirements
Must have
• Modern looking design.

```html
<!DOCTYPE html>
<html lang="en">
<head>
<meta charset="utf-8">
<title>Brisk Current Letterhead</title>
<link href="https://fonts.googleapis.com/css2?family=Heebo:wght@300;400;500&display=swap" rel="stylesheet">
<style>
  :root {
    --orange: #ef7a26;
    --blue: #1f76bc;
    --ink: #1a1a1a;
    --paper: #ffffff;
  }
  * { margin: 0; padding: 0; box-sizing: border-box; }
  html, body { width: 914px; height: 1200px; overflow: hidden; background: var(--paper); }
  .letterhead {
    position: relative;
    width: 914px;
    height: 1200px;
    font-family: "Heebo", Arial, sans-serif;
    color: var(--ink);
    overflow: hidden;
  }
  .wave { position: absolute; left: 0; width: 914px; }
  .wave--top { top: 0; height: 100px; }
  .wave--bottom { bottom: 0; height: 90px; }

  .brand {
    position: absolute;
    left: 110px;
    top: 176px;
    display: flex;
    align-items: center;
    gap: 10px;
  }
  .brand__dot {
    width: 40px; height: 40px;
    border-radius: 50%;
    background: var(--orange);
  }
  .brand__name {
    font-weight: 500;
    font-size: 30px;
    line-height: 30px;
    color: var(--blue);
  }

  .contact {
    position: absolute;
    left: 540px;
    top: 174px;
    width: 300px;
  }
  .contact__row { display: flex; align-items: flex-start; }
  .contact__label {
    width: 103px;
    text-align: right;
    padding-right: 5px;
    font-size: 12px;
    font-weight: 300;
    color: var(--orange);
    line-height: 16px;
  }
  .contact__value {
    font-size: 8px;
    line-height: 12px;
    padding-top: 1px;
    color: var(--ink);
  }
  .contact__row--location { height: 39px; }
  .contact__row--phone { height: 30px; }

  .headline {
    position: absolute;
    left: 108px;
    top: 372px;
    font-size: 18px;
    font-weight: 300;
    letter-spacing: 0.3px;
  }

  .body-copy {
    position: absolute;
    left: 110px;
    top: 421px;
    width: 690px;
    font-size: 12px;
    font-weight: 300;
    line-height: 23.2px;
  }
  .body-copy p { margin-bottom: 23.2px; }
  .body-copy p.tight { margin-bottom: 0; }

  .sign-off {
    position: absolute;
    left: 468px;
    top: 982px;
    width: 326px;
    text-align: center;
    font-size: 12px;
    font-weight: 400;
    line-height: 23.2px;
  }
</style>
</head>
<body>
<div class="letterhead">
  <svg class="wave wave--top" viewBox="0 0 914 100" preserveAspectRatio="none" aria-hidden="true">
    <path d="M0,0 H914 V92 C780,58 600,12 400,14 C210,16 80,48 0,94 Z" fill="var(--orange)"/>
  </svg>

  <div class="brand">
    <span class="brand__dot"></span>
    <span class="brand__name">Brisk<br>Current</span>
  </div>

  <div class="contact">
    <div class="contact__row contact__row--location">
      <span class="contact__label">Location :</span>
      <span class="contact__value">Lorem Ipsum is simply dummy text<br>of the printing and typesetting industry.</span>
    </div>
    <div class="contact__row contact__row--phone">
      <span class="contact__label">Call on :</span>
      <span class="contact__value">121 - 55501928</span>
    </div>
    <div class="contact__row">
      <span class="contact__label">Email :</span>
      <span class="contact__value">hello@briskcurrent.com</span>
    </div>
  </div>

  <h1 class="headline">HEADLINE</h1>

  <div class="body-copy">
    <p>Lorem Ipsum is simply dummy text of the printing and typesetting industry. Lorem Ipsum has been the industry's standard dummy text ever since the 1500s, when an unknown printer took a galley of type and scrambled it to make a type specimen book. It has survived not only five centuries, but also the leap into electronic typesetting, remaining essentially unchanged. It was popularised in the 1960s with the release of Inkvale sheets containing Lorem Ipsum passages, and more recently with desktop publishing software like Folio Layoutpro including versions of Lorem Ipsum.</p>
    <p class="tight">Why do we use it?</p>
    <p>It is a long established fact that a reader will be distracted by the readable content of a page when looking at its layout. The point of using Lorem Ipsum is that it has a more-or-less normal distribution of letters, as opposed to using 'Content here, content here', making it look like readable English. Many desktop publishing packages and web page editors now use Lorem Ipsum as their default model text, and a search for 'lorem ipsum' will uncover many web sites still in their infancy. Various versions have evolved over the years, sometimes by accident, sometimes on purpose (injected humour and the like).</p>
    <p>Lorem Ipsum is simply dummy text of the printing and typesetting industry. Lorem Ipsum has been the industry's standard dummy text ever since the 1500s, when an unknown printer took a galley of type and scrambled it to make a type specimen book. It has survived not only five centuries, but also the leap into electronic typesetting, remaining essentially unchanged. It was popularised in the 1960s with the release of Inkvale sheets containing Lorem Ipsum passages, and more recently with desktop publishing software like Folio Layoutpro including versions of Lorem Ipsum.</p>
    <p class="tight">Why do we use it?</p>
    <p>It is a long established fact that a reader will be distracted by the readable content of a page when looking at its layout.</p>
  </div>

  <p class="sign-off">Lorem Ipsum is simply dummy text of the printing and typesetting industry</p>

  <svg class="wave wave--bottom" viewBox="0 0 914 90" preserveAspectRatio="none" aria-hidden="true">
    <path d="M0,4 C300,0 600,62 760,58 C840,56 890,30 914,2 V90 H0 Z" fill="var(--blue)"/>
  </svg>
</div>
</body>
</html>
```